Start up in business consultancy needs a business card

We need the business card's layout (we have already the logo). Our business is concerned on consultancy services delivered to companies on the matter of sustainability. Business card should be enough essentials and professional style.

Side A with the following info:
logo + a space for the claim (still to identify) + website of the company

Side B with the following info:
Name of business card holder + title of the business card holder + address of the company + space for mobile number, phone number, fax number + e-mail of business card holder + graphic details around.

Target Market(s)

Business of any sector

Industry/Entity Type

Business Service

Contact Information for Business Card

Name of the company:
Pianoverde srl
Società Benefit

Address of the company:
Via Lucerna, 7
21047 - Saronno (VA)

Website:
www.pianoverde.it

Name of the BC' holder:
Luca Ferentino

Title:
Co-fondatore

Email:
luca@pianoverde.it

Mobile:
+39 348 915 2074
Phone:
+39 348 915 2074
Fax:
+39 348 915 2074

Font styles to use
Other font styles liked:
• new gothic

```html
<!DOCTYPE html>
<html lang="it">
<head>
<meta charset="utf-8">
<title>Pianoverde – biglietto da visita</title>
<link href="https://fonts.googleapis.com/css2?family=News+Cycle:wght@400;700&display=swap" rel="stylesheet">
<style>
  :root {
    --brand-blue: #0767ad;
    --paper: #ffffff;
    --ink: #1d1d1b;
    --backdrop: #141414;
  }
  * { box-sizing: border-box; margin: 0; padding: 0; }
  html, body { width: 1200px; height: 741px; overflow: hidden; background: var(--backdrop); }
  body { position: relative; font-family: "News Cycle", "Arial Narrow", sans-serif; }

  .card {
    position: absolute;
    top: 229px;
    width: 494px;
    height: 282px;
    border-radius: 10px;
    overflow: hidden;
  }
  .card--front { left: 100px; background: var(--paper); }
  .card--back  { left: 606px; background: var(--brand-blue); }

  .ring { position: absolute; inset: 0; }

  .wordmark {
    position: absolute;
    display: flex;
    align-items: center;
    gap: 11px;
    font-weight: 400;
    letter-spacing: 0.3px;
    line-height: 1;
  }
  .wordmark__dot { border-radius: 50%; border-style: solid; }
  .card--front .wordmark { left: 27px; top: 19px; color: var(--brand-blue); font-size: 29px; }
  .card--front .wordmark__dot { width: 80px; height: 80px; border-width: 4px; border-color: var(--brand-blue); }
  .card--back .wordmark { left: 216px; top: 174px; color: var(--paper); font-size: 27px; }
  .card--back .wordmark__dot { width: 72px; height: 72px; border-width: 3px; border-color: var(--paper); }

  .holder-band {
    position: absolute;
    left: 0; top: 124px;
    width: 220px; height: 46px;
    background: var(--brand-blue);
    border-radius: 0 7px 7px 0;
    color: var(--paper);
    padding: 8px 0 0 28px;
  }
  .holder-band__name { font-weight: 700; font-size: 19px; line-height: 19px; letter-spacing: -0.3px; }
  .holder-band__role { font-size: 13px; line-height: 14px; }

  .contacts { position: absolute; left: 28px; top: 183px; list-style: none; color: var(--ink); }
  .contacts__item { display: flex; align-items: center; gap: 7px; height: 15.7px; font-size: 13px; }
  .contacts__icon { width: 13px; height: 13px; flex: none; }
  .address { position: absolute; left: 28px; top: 250px; font-size: 13px; color: var(--ink); }

  .website {
    position: absolute;
    right: 32px; top: 236px;
    color: var(--paper);
    font-size: 13px;
  }
</style>
</head>
<body>

  <section class="card card--front" aria-label="Fronte del biglietto">
    <svg class="ring" width="494" height="282" viewBox="0 0 494 282" aria-hidden="true">
      <circle cx="500" cy="140" r="138" fill="none" stroke="var(--brand-blue)" stroke-width="9"/>
    </svg>

    <div class="wordmark"><span class="wordmark__dot"></span><span>pianoverde</span></div>

    <div class="holder-band">
      <p class="holder-band__name">Luca Ferentino</p>
      <p class="holder-band__role">Co-fondatore</p>
    </div>

    <ul class="contacts">
      <li class="contacts__item">
        <svg class="contacts__icon" viewBox="0 0 13 13" aria-label="Cellulare"><rect width="13" height="13" rx="2" fill="var(--brand-blue)"/><rect x="4.2" y="2" width="4.6" height="9" rx="1" fill="#fff"/><rect x="5" y="3" width="3" height="5" fill="var(--brand-blue)"/></svg>
        <span>+39 348 915 2074</span>
      </li>
      <li class="contacts__item">
        <svg class="contacts__icon" viewBox="0 0 13 13" aria-label="Telefono"><rect width="13" height="13" rx="2" fill="var(--brand-blue)"/><path d="M2.5 5.5 Q6.5 2 10.5 5.5 L9.5 6.5 L8 5.5 L5 5.5 L3.5 6.5 Z" fill="#fff"/><rect x="3.5" y="7" width="6" height="3.5" rx="0.8" fill="#fff"/></svg>
        <span>+39 348 915 2074</span>
      </li>
      <li class="contacts__item">
        <svg class="contacts__icon" viewBox="0 0 13 13" aria-label="Fax"><rect width="13" height="13" rx="2" fill="var(--brand-blue)"/><rect x="4" y="2" width="5" height="3" fill="#fff"/><rect x="2.5" y="5.5" width="8" height="4" rx="0.8" fill="#fff"/><rect x="4" y="8.5" width="5" height="2.5" fill="#fff" stroke="var(--brand-blue)" stroke-width="0.6"/></svg>
        <span>+39 348 915 2074</span>
      </li>
      <li class="contacts__item">
        <svg class="contacts__icon" viewBox="0 0 13 13" aria-label="E-mail"><rect width="13" height="13" rx="2" fill="var(--brand-blue)"/><rect x="2.5" y="3.5" width="8" height="6" fill="#fff"/><path d="M2.5 3.5 L6.5 7 L10.5 3.5" fill="none" stroke="var(--brand-blue)" stroke-width="0.8"/></svg>
        <span>luca@pianoverde.it</span>
      </li>
    </ul>

    <p class="address">Via Lucerna, 7 21047 - Saronno (VA)</p>
  </section>

  <section class="card card--back" aria-label="Retro del biglietto">
    <svg class="ring" width="494" height="282" viewBox="0 0 494 282" aria-hidden="true">
      <circle cx="-6" cy="140" r="138" fill="none" stroke="var(--paper)" stroke-width="9"/>
    </svg>

    <div class="wordmark"><span class="wordmark__dot"></span><span>pianoverde</span></div>
    <p class="website">www.pianoverde.it</p>
  </section>

</body>
</html>
```